Tallow Creek Partners needs an email sign off and professional power point template

Newly formed company and we require:1. graphic email signature on our email , and2.a professional powerpoint template (title page and sub pages) and revamp of the attached powerpoint presentation I have uploaded our business car design (logo and contact details ) and a current powerpoint template we are currently working with. Also a brief of how we operateOur mantra is Discover, Develop, Deliver.

Target Market(s)

multinationals and mid size SME's requiring help to grown new markets or geographies for their business.

Colors
000000

Requirements
Must have
• the mantra..our phases of engagement around assisting clients is:
• 1. Discover
• 2. Develop
• 3. Deliver
Nice to have
• we differentiate ourselves form consultant by actually executing the plan for them (i.e. is the delivery phase)

```html
<!DOCTYPE html>
<html lang="en">
<head>
<meta charset="utf-8">
<title>Tallow Creek Partners – Presentation Template</title>
<link href="https://fonts.googleapis.com/css2?family=Arimo:ital,wght@0,400;0,700;1,700&display=swap" rel="stylesheet">
<style>
  :root {
    --navy: #0d2340;
    --navy-deep: #0a1c33;
    --accent: #1a7fb8;
    --accent-bright: #2596d1;
    --paper: #ffffff;
    --ink: #1b1b1b;
    --muted: #8a8a8a;
    --stage-top: #f1f1f1;
    --stage-bottom: #9c9c9c;
  }
  * { box-sizing: border-box; margin: 0; padding: 0; }
  html, body { width: 837px; height: 1200px; overflow: hidden; }
  body { font-family: "Arimo", Arial, sans-serif; background: var(--stage-bottom); }

  .hero {
    position: absolute; left: 0; top: 0; width: 837px; height: 562px;
    background: var(--stage-top);
  }
  .hero .slide { position: absolute; left: 118px; top: 70px; width: 600px; height: 420px; }

  .deck { position: absolute; left: 0; top: 562px; width: 837px; height: 638px; }
  .deck .slide { position: absolute; width: 379px; height: 266px; }
  .deck .s1 { left: 26px; top: 41px; }
  .deck .s2 { left: 433px; top: 41px; }
  .deck .s3 { left: 26px; top: 342px; }
  .deck .s4 { left: 433px; top: 342px; }

  .slide { background: var(--paper); box-shadow: 0 8px 14px rgba(0,0,0,.28); overflow: hidden; }
  .slide svg { display: block; width: 100%; height: 100%; }

  .t-title { font: 700 24px "Arimo", Arial, sans-serif; fill: #fff; }
  .t-date { font: italic 700 15px "Arimo", Arial, sans-serif; fill: #fff; }
  .t-brand { font: 700 50px "Arimo", Arial, sans-serif; fill: #fff; letter-spacing: 2px; }
  .t-brand-sub { font: 700 12px "Arimo", Arial, sans-serif; fill: #fff; letter-spacing: 2px; }
  .t-tag { font: italic 700 11px "Arimo", Arial, sans-serif; fill: #fff; }
  .t-head { font: 400 13px "Arimo", Arial, sans-serif; fill: #fff; }
  .t-foot { font: 400 6.5px "Arimo", Arial, sans-serif; fill: var(--ink); }
  .t-venn { font: 700 11px "Arimo", Arial, sans-serif; fill: var(--ink); }
  .t-bio { font: 400 7px "Arimo", Arial, sans-serif; fill: var(--ink); }
  .t-step { font: 700 8.5px "Arimo", Arial, sans-serif; fill: #fff; }
  .t-mantra { font: 700 17px "Arimo", Arial, sans-serif; fill: var(--accent); }
  .t-mantra-big { font: 700 42px "Arimo", Arial, sans-serif; fill: var(--accent); }
  .head-bar { fill: var(--navy); }
  .head-rule { stroke: var(--accent-bright); stroke-width: 1.5; }
  .foot-rule { stroke: #d0d0d0; stroke-width: .8; }
  .venn { fill: none; stroke: var(--accent); stroke-width: 1.8; }
  .icon { fill: none; stroke: var(--ink); stroke-width: 1.2; stroke-linecap: round; stroke-linejoin: round; }
  .step { fill: var(--navy); stroke: #3a5a80; stroke-width: .8; }
  .arrow { fill: var(--accent); }
  .portrait { fill: #c9c9c9; stroke: #e2e2e2; stroke-width: 3; }
</style>
</head>
<body>

<section class="hero">
  <div class="slide title-slide">
    <svg viewBox="0 0 475 333">
      <defs>
        <linearGradient id="valley-lg" x1="0" y1="0" x2="0" y2="1">
          <stop offset="0" stop-color="#1b8fc6"/>
          <stop offset=".45" stop-color="#175f8f"/>
          <stop offset="1" stop-color="#0c2443"/>
        </linearGradient>
      </defs>
      <rect width="475" height="333" fill="url(#valley-lg)" role="img" aria-label="Photograph of a misty mountain valley in deep blue tones"/>
      <text class="t-title" x="237.5" y="36" text-anchor="middle">TALLOW CREEK PARTNERS</text>
      <text class="t-date" x="237.5" y="58" text-anchor="middle">12th December 2018</text>
      <text class="t-brand" x="237.5" y="175" text-anchor="middle">CAIRN</text>
      <text class="t-brand-sub" x="237.5" y="200" text-anchor="middle">BUSINESS DEVELOPERS</text>
      <text class="t-tag" x="237.5" y="316" text-anchor="middle">Cairn BD - Discover, Develop, Deliver</text>
    </svg>
  </div>
</section>

<section class="deck">
  <div class="slide title-slide s1">
    <svg viewBox="0 0 475 333">
      <defs>
        <linearGradient id="valley-sm" x1="0" y1="0" x2="0" y2="1">
          <stop offset="0" stop-color="#1b8fc6"/>
          <stop offset=".45" stop-color="#175f8f"/>
          <stop offset="1" stop-color="#0c2443"/>
        </linearGradient>
      </defs>
      <rect width="475" height="333" fill="url(#valley-sm)" role="img" aria-label="Photograph of a misty mountain valley in deep blue tones"/>
      <text class="t-title" x="237.5" y="36" text-anchor="middle">TALLOW CREEK PARTNERS</text>
      <text class="t-date" x="237.5" y="58" text-anchor="middle">12th December 2018</text>
      <text class="t-brand" x="237.5" y="175" text-anchor="middle">CAIRN</text>
      <text class="t-brand-sub" x="237.5" y="200" text-anchor="middle">BUSINESS DEVELOPERS</text>
      <text class="t-tag" x="237.5" y="316" text-anchor="middle">Cairn BD - Discover, Develop, Deliver</text>
    </svg>
  </div>

  <div class="slide process-slide s2">
    <svg viewBox="0 0 475 333">
      <rect class="head-bar" width="475" height="33"/>
      <line class="head-rule" x1="0" y1="33.5" x2="475" y2="33.5"/>
      <text class="t-head" x="17" y="21">ALIGNING OUR PROCESS</text>
      <circle class="venn" cx="237" cy="130" r="78"/>
      <circle class="venn" cx="189" cy="208" r="78"/>
      <circle class="venn" cx="286" cy="208" r="78"/>
      <g class="icon">
        <circle cx="237" cy="79" r="5.5"/>
        <path d="M234.5 85v3h5v-3M229 73l-2-2M245 73l2-2M237 70v-3"/>
        <circle cx="160" cy="198" r="5.5"/>
        <path d="M164 202l5 5M155 188l-2-2M160 186v-3M165 188l2-2"/>
        <rect x="300" y="190" width="12" height="11"/>
        <path d="M312 194h5l3 4v3h-8M303 195l2 2 4-4"/>
        <circle cx="304" cy="203" r="1.6"/><circle cx="316" cy="203" r="1.6"/>
      </g>
      <text class="t-venn" x="237" y="113" text-anchor="middle">DEVELOP</text>
      <text class="t-venn" x="158" y="229" text-anchor="middle">DISCOVER</text>
      <text class="t-venn" x="316" y="229" text-anchor="middle">DELIVER</text>
      <line class="foot-rule" x1="17" y1="309" x2="445" y2="309"/>
      <text class="t-foot" x="17" y="322">Cairn BD - Discover, Develop, Deliver</text>
      <text class="t-foot" x="447" y="312">02</text>
    </svg>
  </div>

  <div class="slide team-slide s3">
    <svg viewBox="0 0 475 333">
      <rect class="head-bar" width="475" height="33"/>
      <line class="head-rule" x1="0" y1="33.5" x2="475" y2="33.5"/>
      <text class="t-head" x="17" y="21">THREE DIRECTORS EXPERIENCE</text>
      <circle class="portrait" cx="86" cy="148" r="41" role="img" aria-label="Director portrait placeholder"/>
      <circle class="portrait" cx="237" cy="148" r="41" role="img" aria-label="Director portrait placeholder"/>
      <circle class="portrait" cx="389" cy="148" r="41" role="img" aria-label="Director portrait placeholder"/>
      <text class="t-bio" text-anchor="middle">
        <tspan x="86" y="205">Two decades growing new</tspan>
        <tspan x="86" y="215">markets for global industrial</tspan>
        <tspan x="86" y="225">brands.</tspan>
      </text>
      <text class="t-bio" text-anchor="middle">
        <tspan x="237" y="205">Led regional expansion for</tspan>
        <tspan x="237" y="215">mid size firms across</tspan>
        <tspan x="237" y="225">Europe.</tspan>
      </text>
      <text class="t-bio" text-anchor="middle">
        <tspan x="389" y="205">Built partner networks and</tspan>
        <tspan x="389" y="215">sales teams in Asia</tspan>
        <tspan x="389" y="225">Pacific.</tspan>
      </text>
      <line class="foot-rule" x1="17" y1="309" x2="445" y2="309"/>
      <text class="t-foot" x="17" y="322">Cairn BD - Discover, Develop, Deliver</text>
      <text class="t-foot" x="447" y="312">03</text>
    </svg>
  </div>

  <div class="slide plan-slide s4">
    <svg viewBox="0 0 475 333">
      <rect class="head-bar" width="475" height="33"/>
      <line class="head-rule" x1="0" y1="33.5" x2="475" y2="33.5"/>
      <text class="t-head" x="17" y="21">OPPORTUNITY PLANNING PROCESS</text>

      <rect class="step" x="45" y="61" width="87" height="50" rx="5"/>
      <text class="t-step" text-anchor="middle"><tspan x="88.5" y="83">Identify</tspan><tspan x="88.5" y="94">Opportunity</tspan></text>
      <rect class="step" x="176" y="61" width="87" height="50" rx="5"/>
      <text class="t-step" text-anchor="middle"><tspan x="219.5" y="77">Qualify</tspan><tspan x="219.5" y="88">Opportunity</tspan><tspan x="219.5" y="99">(Discover)</tspan></text>
      <rect class="step" x="306" y="61" width="123" height="50" rx="5"/>
      <text class="t-step" text-anchor="middle"><tspan x="367.5" y="77">Identify Key Individuals</tspan><tspan x="367.5" y="88">of Influence to Decision</tspan><tspan x="367.5" y="99">Process</tspan></text>
      <rect class="step" x="306" y="145" width="123" height="50" rx="5"/>
      <text class="t-step" text-anchor="middle"><tspan x="367.5" y="161">Develop &amp; Implement</tspan><tspan x="367.5" y="172">Sales</tspan><tspan x="367.5" y="183">Strategy &amp; Plan</tspan></text>
      <rect class="step" x="306" y="226" width="123" height="50" rx="5"/>
      <text class="t-step" text-anchor="middle"><tspan x="367.5" y="242">Align &amp; Develop</tspan><tspan x="367.5" y="253">Relationships with Key</tspan><tspan x="367.5" y="264">people of Influence</tspan></text>
      <rect class="step" x="176" y="226" width="87" height="50" rx="5"/>
      <text class="t-step" text-anchor="middle"><tspan x="219.5" y="242">Execute Plan</tspan><tspan x="219.5" y="253">And Deliver</tspan><tspan x="219.5" y="264">Proposal</tspan></text>
      <rect class="step" x="45" y="226" width="87" height="50" rx="5"/>
      <text class="t-step" text-anchor="middle"><tspan x="88.5" y="248">Negotiate</tspan><tspan x="88.5" y="259">and Sign</tspan></text>

      <path class="arrow" d="M148 83h7v-3.5l6 5.5-6 5.5v-3.5h-7z"/>
      <path class="arrow" d="M279 83h7v-3.5l6 5.5-6 5.5v-3.5h-7z"/>
      <path class="arrow" d="M365 121v7h-3.5l5.5 6 5.5-6h-3.5v-7z"/>
      <path class="arrow" d="M365 205v7h-3.5l5.5 6 5.5-6h-3.5v-7z"/>
      <path class="arrow" d="M292 248h-7v-3.5l-6 5.5 6 5.5v-3.5h7z"/>
      <path class="arrow" d="M161 248h-7v-3.5l-6 5.5 6 5.5v-3.5h7z"/>

      <text class="t-mantra" x="61" y="150">DISCOVER, DEVELOP,</text>
      <text class="t-mantra-big" x="60" y="194">DELIVER</text>

      <line class="foot-rule" x1="17" y1="309" x2="445" y2="309"/>
      <text class="t-foot" x="17" y="322">Cairn BD - Discover, Develop, Deliver</text>
      <text class="t-foot" x="447" y="312">04</text>
    </svg>
  </div>
</section>

</body>
</html>
```